Hammerleaf Workshop 2021 Norvell Castara full vehicle wrap

We were playing around with ideas here that I’ve attached – I like nothing about these of the van that were created for us. We want, big/bold/colorful but not tacky. I was thinking one color for the whole thing, but if we go with a light color from our colors in the logo, then we can’t have the logo on top as that will drown out a piece of the logo unless there is a bit of color distortion where the logo is if you understand what I mean.
Our company is a commercial school that offers classes to homeowner’s teaching them how to do their own home renovations. I was liking the idea of using pictures so that it shows real people at our training center but it has to be really clear what they are doing. We have tons of pictures and have just added a few here. We don’t want just plain tools or anything on the design as we don’t want people to think we are contractors. We want them to understand what Hammerleaf Workshop is. Our tagline is “Build Every Room With Grit”, but really, it should be “Learn to do your own renos” on the van so that people know exactly what we do. I was thinking that we can remove the backgrounds of some of our pictures so that there is more focus for the people in the pictures.
I think for the back of the van, we could have “Learn to reno classes” and then a list of classes that we offer such as
Tiling
Flooring
Framing
Finishing
Plumbing
Electrical
Maintenance
Accent Walls
Drywall
Kitchen cabinets
I know that list is too big so we would have to just pick some and write & more or something.
We are most likely getting a 1800 number for the vehicle. But don’t have it yet so my cell phone can be used in the meantime but will be getting one prior to the wrap being done. And our website is www.hammerleafworkshop.com.
We are also thinking to stay away from being too busy, we could go with a bright color that would still work with our branding and be minimalistic with the pictures and wording. Such as the Brambleton pictures here in bright green.
This is a 2021 Norvell Castara.
I’ve also attached pictures that I googled for inspiration.

```html
<!DOCTYPE html>
<html lang="en">
<head>
<meta charset="utf-8">
<title>Hammerleaf Workshop – Norvell Castara Vehicle Wrap</title>
<link rel="stylesheet" href="https://fonts.googleapis.com/css2?family=Oswald:wght@500;600&family=Montserrat:wght@500;600;700&display=swap">
<style>
  :root {
    --bg: #ebebeb;
    --body: #fbfbfa;
    --body-shade: #dcdcdc;
    --teal: #1f6b70;
    --teal-light: #5f9c9c;
    --gold: #b5862c;
    --ink: #2c3a3d;
    --glass: #3a3d40;
    --tyre: #1e1f21;
    --rim: #b9bcbf;
    --tail: #a8202b;
    --white: #ffffff;
  }
  html, body {
    margin: 0;
    padding: 0;
    width: 1200px;
    height: 1200px;
    overflow: hidden;
    background: var(--bg);
  }
  .wrap-sheet { display: block; width: 1200px; height: 1200px; }
  .list-item { font-family: "Oswald", sans-serif; font-weight: 600; fill: var(--ink); }
  .list-item.on-teal { fill: var(--white); }
  .bullet { fill: var(--gold); }
  .brand-name { font-family: "Montserrat", sans-serif; font-weight: 700; fill: var(--teal); }
  .brand-name.on-teal { fill: var(--white); }
  .tagline { font-family: "Montserrat", sans-serif; font-weight: 500; fill: var(--teal); }
  .tagline.on-teal { fill: var(--white); }
  .phone { font-family: "Montserrat", sans-serif; font-weight: 600; }
  .url { font-family: "Montserrat", sans-serif; font-weight: 600; fill: var(--gold); }
  .slogan { font-family: "Oswald", sans-serif; font-weight: 500; letter-spacing: 1px; }
</style>
</head>
<body>
<svg class="wrap-sheet" viewBox="0 0 1200 1200" xmlns="http://www.w3.org/2000/svg">
  <defs>
    <linearGradient id="photo-warm" x1="0" y1="0" x2="1" y2="1">
      <stop offset="0" stop-color="#d8c3a5"/>
      <stop offset="1" stop-color="#8c7660"/>
    </linearGradient>
    <linearGradient id="photo-cool" x1="0" y1="0" x2="1" y2="1">
      <stop offset="0" stop-color="#b7bcb8"/>
      <stop offset="1" stop-color="#5e6966"/>
    </linearGradient>
    <linearGradient id="teal-fade" x1="0" y1="0" x2="1" y2="0">
      <stop offset="0" stop-color="var(--teal)"/>
      <stop offset="1" stop-color="var(--teal-light)"/>
    </linearGradient>
    <linearGradient id="rear-glass" x1="0" y1="0" x2="1" y2="0">
      <stop offset="0" stop-color="#ffffff"/>
      <stop offset="0.55" stop-color="#e6e1d8"/>
      <stop offset="1" stop-color="#c9b59a"/>
    </linearGradient>
  </defs>

  <!-- Side view -->
  <g class="side-view">
    <path class="van-body" fill="var(--body)" stroke="var(--body-shade)" stroke-width="2"
      d="M45 440 Q40 385 70 360 L160 325 Q240 290 300 235 Q360 185 440 172 L1070 162 Q1120 165 1150 215 Q1175 270 1172 340 L1170 470 Q1168 505 1140 512 L80 515 Q48 510 45 480 Z"/>
    <path class="front-glass" fill="var(--glass)" d="M310 290 Q360 220 440 200 L590 196 L590 285 Z"/>
    <path class="mirror" fill="#cfcfcf" d="M390 295 L425 290 L428 320 L395 322 Z"/>

    <path class="band-teal" fill="url(#teal-fade)"
      d="M350 470 L780 470 Q960 430 1060 340 L1172 300 L1170 470 Q1168 505 1140 512 L350 512 Z"/>
    <path class="band-gold" fill="var(--gold)"
      d="M570 515 Q820 480 1050 330 L1172 285 L1172 310 L1060 350 Q860 490 640 515 Z"/>

    <path role="img" aria-label="Photo of smiling students at a renovation class" fill="url(#photo-warm)"
      d="M985 185 L1120 168 Q1150 200 1160 260 L1160 330 L1060 370 Q1010 400 990 400 Z"/>

    <circle cx="935" cy="240" r="60" fill="var(--gold)"/>
    <circle role="img" aria-label="Photo of students fitting drywall" cx="935" cy="240" r="53" fill="url(#photo-cool)"/>
    <circle cx="870" cy="362" r="58" fill="var(--gold)"/>
    <circle role="img" aria-label="Photo of a student laying floor tile" cx="870" cy="362" r="51" fill="url(#photo-cool)"/>
    <circle cx="778" cy="448" r="60" fill="var(--gold)"/>
    <circle role="img" aria-label="Photo of students at a framing workbench" cx="778" cy="448" r="53" fill="url(#photo-warm)"/>

    <g class="class-list" font-size="16">
      <circle class="bullet" cx="634" cy="203" r="3.5"/><text class="list-item" x="641" y="209">TILING</text>
      <circle class="bullet" cx="634" cy="222" r="3.5"/><text class="list-item" x="641" y="228">FLOORING</text>
      <circle class="bullet" cx="634" cy="241" r="3.5"/><text class="list-item" x="641" y="247">FRAMING</text>
      <circle class="bullet" cx="634" cy="260" r="3.5"/><text class="list-item" x="641" y="266">FINISHING</text>
      <circle class="bullet" cx="634" cy="279" r="3.5"/><text class="list-item" x="641" y="285">PLUMBING</text>
      <circle class="bullet" cx="720" cy="203" r="3.5"/><text class="list-item" x="727" y="209">ELECTRICAL</text>
      <circle class="bullet" cx="720" cy="222" r="3.5"/><text class="list-item" x="727" y="228">MAINTENANCE</text>
      <circle class="bullet" cx="720" cy="241" r="3.5"/><text class="list-item" x="727" y="247">ACCENT WALLS</text>
      <circle class="bullet" cx="720" cy="260" r="3.5"/><text class="list-item" x="727" y="266">DRYWALL</text>
      <circle class="bullet" cx="720" cy="279" r="3.5"/><text class="list-item" x="727" y="285">KITCHEN CABINETS</text>
    </g>
    <text class="url" x="622" y="310" font-size="14">www.hammerleafworkshop.com</text>

    <text class="slogan" x="160" y="360" font-size="16" fill="var(--teal)">LEARN TO DO YOUR OWN RENOS</text>
    <rect x="370" y="392" width="22" height="22" fill="var(--teal)"/>
    <text class="brand-name" x="400" y="412" font-size="24">Hammerleaf Workshop</text>
    <text class="tagline" x="370" y="444" font-size="19">Build Every Room With Grit</text>
    <text class="phone" x="370" y="498" font-size="34" fill="#ffffff">1800 number</text>

    <circle cx="238" cy="478" r="78" fill="var(--tyre)"/>
    <circle cx="238" cy="478" r="50" fill="var(--rim)"/>
    <circle cx="238" cy="478" r="14" fill="#7d8083"/>
    <circle cx="950" cy="478" r="78" fill="var(--tyre)"/>
    <circle cx="950" cy="478" r="50" fill="var(--rim)"/>
    <circle cx="950" cy="478" r="14" fill="#7d8083"/>
    <path fill="#555" d="M62 362 L130 345 L125 360 L70 372 Z"/>
    <path fill="var(--tail)" d="M1130 220 L1160 240 L1165 275 L1140 265 Z"/>
  </g>

  <!-- Rear view A -->
  <g class="rear-view rear-a" transform="translate(30 725)">
    <path fill="var(--body)" stroke="var(--body-shade)" stroke-width="2"
      d="M70 10 L270 10 Q300 40 310 110 L330 130 L330 265 L10 265 L10 130 L30 110 Q40 40 70 10 Z"/>
    <path fill="var(--teal)" d="M72 14 L268 14 Q292 40 300 105 L40 105 Q48 40 72 14 Z"/>
    <path role="img" aria-label="Photo of smiling students" fill="url(#rear-glass)" d="M196 18 L266 18 Q288 45 296 100 L196 100 Z"/>
    <rect x="78" y="32" width="13" height="13" fill="var(--white)"/>
    <text class="brand-name on-teal" x="96" y="44" font-size="13">Hammerleaf</text>
    <text class="brand-name on-teal" x="78" y="62" font-size="13">Workshop</text>
    <text class="tagline on-teal" x="78" y="76" font-size="8">Build Every Room With Grit</text>
    <rect x="10" y="105" width="320" height="20" fill="var(--tail)"/>
    <rect x="145" y="132" width="50" height="20" fill="#222"/>
    <path fill="var(--gold)" d="M10 150 Q170 120 330 150 L330 162 Q170 135 10 165 Z"/>
    <text class="phone" x="30" y="198" font-size="17" fill="var(--ink)">1800 number</text>
    <text class="url" x="30" y="212" font-size="8">www.hammerleafworkshop.com</text>
    <g font-size="8">
      <text class="list-item" x="180" y="188">• TILING</text>
      <text class="list-item" x="180" y="198">• FLOORING</text>
      <text class="list-item" x="180" y="208">• FRAMING</text>
      <text class="list-item" x="180" y="218">• FINISHING</text>
      <text class="list-item" x="180" y="228">• PLUMBING</text>
      <text class="list-item" x="236" y="188">• ELECTRICAL</text>
      <text class="list-item" x="236" y="198">• MAINTENANCE</text>
      <text class="list-item" x="236" y="208">• ACCENT WALLS</text>
      <text class="list-item" x="236" y="218">• DRYWALL</text>
      <text class="list-item" x="236" y="228">• KITCHEN CABINETS</text>
    </g>
    <text class="slogan" x="170" y="252" font-size="11" fill="var(--gold)" text-anchor="middle">LEARN TO DO YOUR OWN RENOS</text>
    <rect x="10" y="265" width="45" height="35" rx="4" fill="var(--tyre)"/>
    <rect x="285" y="265" width="45" height="35" rx="4" fill="var(--tyre)"/>
  </g>

  <!-- Rear view B -->
  <g class="rear-view rear-b" transform="translate(430 725)">
    <path fill="var(--body)" stroke="var(--body-shade)" stroke-width="2"
      d="M70 10 L270 10 Q300 40 310 110 L330 130 L330 265 L10 265 L10 130 L30 110 Q40 40 70 10 Z"/>
    <path fill="var(--teal)" d="M72 14 L268 14 Q292 40 300 105 L40 105 Q48 40 72 14 Z"/>
    <path role="img" aria-label="Photo of smiling students" fill="url(#rear-glass)" d="M212 18 L266 18 Q288 45 296 100 L212 100 Z"/>
    <g font-size="8.5">
      <text class="list-item on-teal" x="64" y="38">• TILING</text>
      <text class="list-item on-teal" x="64" y="50">• FLOORING</text>
      <text class="list-item on-teal" x="64" y="62">• FRAMING</text>
      <text class="list-item on-teal" x="64" y="74">• FINISHING</text>
      <text class="list-item on-teal" x="64" y="86">• PLUMBING</text>
      <text class="list-item on-teal" x="124" y="38">• ELECTRICAL</text>
      <text class="list-item on-teal" x="124" y="50">• MAINTENANCE</text>
      <text class="list-item on-teal" x="124" y="62">• ACCENT WALLS</text>
      <text class="list-item on-teal" x="124" y="74">• DRYWALL</text>
      <text class="list-item on-teal" x="124" y="86">• KITCHEN CABINETS</text>
    </g>
    <rect x="10" y="105" width="320" height="20" fill="var(--tail)"/>
    <rect x="145" y="132" width="50" height="20" fill="#222"/>
    <path fill="var(--gold)" d="M10 150 Q170 120 330 150 L330 162 Q170 135 10 165 Z"/>
    <rect x="30" y="180" width="12" height="12" fill="var(--teal)"/>
    <text class="brand-name" x="46" y="191" font-size="12">Hammerleaf</text>
    <text class="brand-name" x="30" y="206" font-size="12">Workshop</text>
    <text class="tagline" x="30" y="219" font-size="8">Build Every Room With Grit</text>
    <text class="phone" x="180" y="198" font-size="17" fill="var(--ink)">1800 number</text>
    <text class="url" x="180" y="212" font-size="8">www.hammerleafworkshop.com</text>
    <text class="slogan" x="170" y="252" font-size="11" fill="var(--gold)" text-anchor="middle">LEARN TO DO YOUR OWN RENOS</text>
    <rect x="10" y="265" width="45" height="35" rx="4" fill="var(--tyre)"/>
    <rect x="285" y="265" width="45" height="35" rx="4" fill="var(--tyre)"/>
  </g>

  <!-- Front view -->
  <g class="front-view" transform="translate(825 725)">
    <path fill="var(--body)" stroke="var(--body-shade)" stroke-width="2"
      d="M60 15 L280 15 Q305 40 318 100 L335 120 L335 265 L5 265 L5 120 L22 100 Q35 40 60 15 Z"/>
    <path fill="var(--glass)" d="M62 22 L278 22 Q298 50 306 95 L34 95 Q42 50 62 22 Z"/>
    <rect x="64" y="120" width="10" height="10" fill="var(--teal)"/>
    <text class="brand-name" x="78" y="130" font-size="14">Hammerleaf Workshop</text>
    <text class="tagline" x="64" y="146" font-size="10">Build Every Room With Grit</text>
    <path fill="#555" d="M20 160 L85 172 L80 182 L22 178 Z"/>
    <path fill="#555" d="M320 160 L255 172 L260 182 L318 178 Z"/>
    <rect x="100" y="168" width="140" height="45" rx="10" fill="var(--glass)"/>
    <rect x="145" y="222" width="50" height="20" fill="#222"/>
    <rect x="85" y="232" width="170" height="24" rx="6" fill="var(--glass)"/>
    <rect x="8" y="265" width="45" height="35" rx="4" fill="var(--tyre)"/>
    <rect x="287" y="265" width="45" height="35" rx="4" fill="var(--tyre)"/>
  </g>
</svg>
</body>
</html>
```